Rollo Penwick Design, LLC (www.rollopenwick.example)

A very hip, trendy architectural home page. Simple Menu upper right hand corner (About, Projects, Inspiration, Design-Build, Contact). In the "Projects" ... I want to click on each project and that will open up multiple photo's of that project. Attached are the graphics of my logo. I want the home page to be incredible ... I really market my name "Rollo Penwick" as sophisticated architecture. Colors/branding should be black/metallic/white/grey maybe with a pop of a bright color but not much. My architecture is like www.brantleyhoweatelier.example if you want to review as example. My specialty is industrial design, homes with architectural concrete design, steel beams, alot of glass. Very modern. My work is best illustrated at www.varnellquist.example.
Updates

Please see images uploaded in my brief. A new business card design by an AWESOME designer and some inspirational architectural projects I worked on.

Industry/Entity Type

Architecture

Coding

Coded - Design and coding required

Number of Pages Required

5+ page

Colors

Designer to choose only greyscale colors for use in the design.

Requirements
Must have
• The 1st project photo gallery is called "Foundry Dwelling by the Gulf Shore"... Images of this project can be taken from: https://www.hearthlisto.example/homedetails/2873-9th-St-SE-Naples-FL-34102/508164290_zpid/

The 2nd project photo gallery is called "Stone, Iron and Pane Residences of the Gulf Shore". I will upload images for this project but use placeholder until I finalize.

The 3rd photo gallery is called "Early Sketches: Off the Drafting Table". I will forward pictures. for this.

Website should be easy to update and handover at completion as we will be updating frequently. Wordpress, WIX, or other type is fine as long as it looks profesional and high-class.
Nice to have
• Maybe the home page loads to just "Rollo Penwick Design, LLC ... Workshop of Inventive Structural Vision" and has a click to enter button. Something cool maybe a fade it or something eye-catching and cool.
Should not have
• Should not be overly colorful.

```html
<!DOCTYPE html>
<html lang="en">
<head>
<meta charset="utf-8">
<title>Rollo Penwick Design, LLC</title>
<link href="https://fonts.googleapis.com/css2?family=Arimo:wght@400;700&family=Open+Sans:ital,wght@1,700&display=swap" rel="stylesheet">
<style>
:root{
  --accent:#e4511c;
  --ink:#111111;
  --text:#333333;
  --muted:#555555;
  --band:#f1eff0;
  --rule:#c8c8c8;
  --footer:#141414;
  --field:#9a9a9a;
  --white:#ffffff;
}
*{margin:0;padding:0;box-sizing:border-box}
html,body{width:1200px;height:3808px;overflow:hidden}
body{position:relative;background:var(--white);font-family:"Arimo",Arial,sans-serif;color:var(--text)}
.abs{position:absolute}

/* header */
.site-header{position:absolute;left:0;top:0;width:1200px;height:163px;background:var(--white)}
.brand-square{left:58px;top:62px;width:56px;height:56px;border:4px solid var(--ink)}
.brand-divider{left:128px;top:40px;width:2px;height:108px;background:var(--ink)}
.brand-name{left:146px;top:78px;font-size:21px;color:var(--ink);letter-spacing:.5px;white-space:nowrap}
.main-nav a{position:absolute;top:92px;font-size:13.5px;color:var(--ink);text-decoration:none;letter-spacing:.4px;transform:translateX(-50%);white-space:nowrap}
.main-nav a.active{color:var(--accent)}
.nav-mark{position:absolute;top:68px;width:12px;height:12px;border:2px solid #b9b9b9;transform:translateX(-50%)}
.nav-mark.active{border-color:var(--accent)}

/* hero */
.hero{left:0;top:163px;width:1200px;height:493px;background:linear-gradient(180deg,#f4f4f4 0%,#dcdcdc 45%,#b9b9b9 70%,#e2e2e2 100%)}
.hero-structure{right:0;top:25px;width:480px;height:468px;background:linear-gradient(90deg,rgba(30,30,30,0) 0%,rgba(30,30,30,.55) 35%,#2a2a2a 100%)}
.hero-title{left:158px;top:126px;font-family:"Open Sans",sans-serif;font-style:italic;font-weight:700;font-size:44px;line-height:58px;color:#1c1c1c;letter-spacing:1.5px}

/* about */
.about-square{left:163px;top:770px;width:150px;height:160px;border:8px solid var(--ink)}
.about-divider{left:342px;top:709px;width:2px;height:280px;background:var(--ink)}
.about-title{left:415px;top:722px;font-size:47px;color:var(--ink);letter-spacing:.5px}
.about-copy{left:415px;top:798px;width:600px;font-size:13.5px;line-height:24px;color:var(--text)}
.btn-outline{left:414px;top:916px;width:138px;height:45px;border:1px solid var(--accent);color:var(--accent);font-size:14px;display:flex;align-items:center;justify-content:center}

/* services */
.services{left:0;top:1057px;width:1200px;height:428px;background:var(--band)}
.service{position:absolute;top:1130px;width:250px}
.service h3{font-weight:400;font-size:28px;line-height:34px;color:var(--ink)}
.service .underline{width:103px;height:1.5px;background:var(--accent);margin-top:14px}
.service p{margin-top:16px;width:240px;font-size:13.5px;line-height:19px;color:var(--text);text-align:justify}
.btn-solid{margin-top:30px;width:127px;height:40px;background:var(--accent);color:var(--white);font-size:14px;display:flex;align-items:center;justify-content:center}

/* section headings */
.section-head{position:absolute;left:0;width:1200px;height:124px}
.section-head .mark{position:absolute;width:88px;height:92px;border:5px solid var(--ink);top:16px}
.section-head .rule{position:absolute;width:2px;height:124px;top:0;background:var(--ink)}
.section-head h2{position:absolute;top:34px;font-weight:400;font-size:50px;color:var(--ink);letter-spacing:1px}

/* projects */
.project-photo{position:absolute;width:445px;height:302px}
.project-text{position:absolute;width:392px}
.project-text h3{font-weight:400;font-size:28px;line-height:38px;color:#2a2a2a}
.project-text p{margin-top:12px;font-size:13.5px;line-height:24px;color:var(--text)}
.project-text .rule{height:1px;background:var(--rule);margin-top:12px}
.project-text .know{display:block;margin-top:20px;font-weight:700;font-size:19px;color:var(--accent);letter-spacing:.5px}
.project-text .rule.end{margin-top:20px}

/* gallery */
.gallery{left:0;top:2898px;width:1200px;height:566px;background:var(--band)}
.thumb{position:absolute;top:3154px;width:211px;height:214px}

/* footer */
.site-footer{left:0;top:3464px;width:1200px;height:344px;background:var(--footer)}
.footer-title{position:absolute;top:3524px;font-size:25px;color:var(--white);letter-spacing:1px}
.footer-info{left:143px;font-size:13.5px;line-height:19px;color:var(--white)}
.field{background:var(--field);color:#ececec;font-size:12px;padding:0 10px;display:flex;align-items:center;letter-spacing:.5px}
.field.message{align-items:flex-start;padding-top:12px}
.footer-rule{left:143px;top:3701px;width:744px;height:1px;background:#cfcfcf}
.btn-send{left:906px;top:3680px;width:148px;height:34px;background:var(--accent);color:var(--white);font-size:14px;letter-spacing:1px;display:flex;align-items:center;justify-content:center}
.copyright{left:143px;top:3728px;font-size:13.5px;color:var(--white)}
</style>
</head>
<body>

<header class="site-header">
  <div class="abs brand-square"></div>
  <div class="abs brand-divider"></div>
  <div class="abs brand-name">Rollo Penwick Design, LLC</div>
  <nav class="main-nav">
    <span class="nav-mark active" style="left:638px"></span><a class="active" style="left:638px">ABOUT</a>
    <span class="nav-mark" style="left:737px"></span><a style="left:737px">PROJECTS</a>
    <span class="nav-mark" style="left:856px"></span><a style="left:856px">INSPIRATION</a>
    <span class="nav-mark" style="left:989px"></span><a style="left:989px">DESIGN-BUILD</a>
    <span class="nav-mark" style="left:1109px"></span><a style="left:1109px">CONTACT</a>
  </nav>
</header>

<section class="abs hero" role="img" aria-label="Black and white photograph of a steel-framed modern structure reflected on a wide glassy plaza">
  <div class="abs hero-structure"></div>
  <h1 class="abs hero-title">Workshop of Inventive<br>&nbsp;Structural Vision</h1>
</section>

<section class="about">
  <div class="abs about-square"></div>
  <div class="abs about-divider"></div>
  <h2 class="abs about-title">ABOUT US</h2>
  <p class="abs about-copy">Lorem Ipsum is simply dummy text of the printing and typesetting industry. Lorem Ipsum has been the industry's standard dummy text ever since the 1500s, when an unknown printer took a galley of type and scrambled it to make a type specimen book. Lorem Ipsum is simply dummy text of the printing and typesetting industry.</p>
  <div class="abs btn-outline">Read More</div>
</section>

<section class="abs services"></section>
<div class="service" style="left:145px">
  <h3>Industrial<br>Design</h3>
  <div class="underline"></div>
  <p>Lorem Ipsum has been the industry's standard dummy text ever since the when an unknown printer took a galley of type and scrambled it to make a type specimen book.</p>
  <div class="btn-solid">Read More</div>
</div>
<div class="service" style="left:452px">
  <h3>Architectural<br>Concrete Design</h3>
  <div class="underline"></div>
  <p>Lorem Ipsum has been the industry's standard dummy text ever since the 1500s, when an unknown printer took a galley of type and scrambled it to make a type specimen book.</p>
  <div class="btn-solid">Read More</div>
</div>
<div class="service" style="left:767px">
  <h3>Steel<br>Beams</h3>
  <div class="underline"></div>
  <p>Lorem Ipsum has been the industry's standard dummy text ever since the 1500s, when an unknown printer took a galley of type and scrambled it to make a type specimen book.</p>
  <div class="btn-solid">Read More</div>
</div>

<div class="section-head" style="top:1543px">
  <div class="mark" style="left:397px"></div>
  <div class="rule" style="left:501px"></div>
  <h2 style="left:523px">PROJECTS</h2>
</div>

<div class="project-photo" style="left:143px;top:1754px;background:linear-gradient(180deg,#2f6fd0 0%,#8fb0d8 40%,#c9b79a 62%,#3f7a2c 85%,#2f6a22 100%)" role="img" aria-label="Photograph of a long modern concrete house with a pool and lawn at dusk"></div>
<div class="project-text" style="left:665px;top:1768px">
  <h3>Foundry Dwelling by the Gulf Shore</h3>
  <p>Lorem Ipsum is simply dummy text of the printing and typesetting industry. Lorem Ipsum has been the industry's standard dummy text ever since the 1500s, when an unknown printer took a galley of type aspecimen book.</p>
  <div class="rule"></div>
  <span class="know">KNOW MORE</span>
  <div class="rule end"></div>
</div>

<div class="project-text" style="left:143px;top:2136px">
  <h3>Stone, Iron and Pane Residences of the Gulf Shore</h3>
  <p>Lorem Ipsum is simply dummy text of the printing and typesetting industry. Lorem Ipsum has been the industry's standard dummy text ever since the 1500s, when an unknown printer took a galley of type aspecimen book.</p>
  <div class="rule"></div>
  <span class="know">KNOW MORE</span>
  <div class="rule end"></div>
</div>
<div class="project-photo" style="left:610px;top:2130px;background:linear-gradient(180deg,#1d4fb8 0%,#3a6bc4 25%,#b8a35a 45%,#a8934e 70%,#2b2b25 88%,#2d5a22 100%)" role="img" aria-label="Photograph of a square concrete facade with a lit glass entrance at night"></div>

<div class="project-photo" style="left:143px;top:2498px;background:linear-gradient(180deg,#5b9be0 0%,#a9c9ea 30%,#bdbdb4 50%,#4d7f34 72%,#5e9a36 100%)" role="img" aria-label="Photograph of a modern concrete house beside a pavilion on a green lawn"></div>
<div class="project-text" style="left:665px;top:2512px">
  <h3>Early Sketches: Off the Drafting Table</h3>
  <p>Lorem Ipsum is simply dummy text of the printing and typesetting industry. Lorem Ipsum has been the industry's standard dummy text ever since the 1500s, when an unknown printer took a galley of type aspecimen book.</p>
  <div class="rule"></div>
  <span class="know">KNOW MORE</span>
  <div class="rule end"></div>
</div>

<section class="abs gallery"></section>
<div class="section-head" style="top:2962px">
  <div class="mark" style="left:397px"></div>
  <div class="rule" style="left:501px"></div>
  <h2 style="left:523px">GALLERY</h2>
</div>
<div class="thumb" style="left:142px;background:linear-gradient(180deg,#4a3a30 0%,#d8d2ca 45%,#c9b8a4 100%)" role="img" aria-label="Photograph of a bedroom with exposed beams and tall glass doors"></div>
<div class="thumb" style="left:377px;background:linear-gradient(180deg,#3d3d3d 0%,#4f7f3a 35%,#6fb3c8 60%,#cfcfcf 100%)" role="img" aria-label="Photograph of lounge chairs on a covered patio facing a pool"></div>
<div class="thumb" style="left:612px;background:linear-gradient(180deg,#1e4fc0 0%,#2a5bc8 45%,#6a4fc4 70%,#2f5a22 100%)" role="img" aria-label="Photograph of a lit pool leading to a modern house at night"></div>
<div class="thumb" style="left:848px;background:linear-gradient(180deg,#7a5a3e 0%,#5a8a45 35%,#d8d8d8 65%,#bfbfbf 100%)" role="img" aria-label="Photograph of an outdoor dining terrace under a wooden roof"></div>

<footer class="abs site-footer"></footer>
<h3 class="footer-title" style="left:140px;font-weight:400">GET IN TOUCH</h3>
<h3 class="footer-title" style="left:613px;font-weight:400">CONTACT US</h3>
<p class="abs footer-info" style="top:3587px">Tel: 555.014.2286<br>Email: rollo@rollopenwick.example</p>
<p class="abs footer-info" style="top:3640px">4180 Marlowe Crest Road<br>Suite 212, Naples FL 34100</p>
<div class="abs field" style="left:613px;top:3587px;width:210px;height:30px">Enter your name</div>
<div class="abs field" style="left:613px;top:3636px;width:210px;height:29px">Enter your &nbsp;email</div>
<div class="abs field message" style="left:845px;top:3587px;width:209px;height:77px">Enter your message</div>
<div class="abs footer-rule"></div>
<div class="abs btn-send">SEND</div>
<p class="abs copyright">All Rights Reserved © 2021 by Rollo Penwick.</p>

</body>
</html>
```